Powerpoint to present for client our social media services along with a test case

we need a powerpoint template design that is modern looking and eye catching and keeps the client engaged. we are a social media agency based in Kuwait so the content will be bilingual in english and in Arabic. i will be providing the logo and you can design based upon the logo provided. the main tasks for this PPT is to show case our case studies and for sales presentation. the presentations will be a mix of visuals, texts, graphs and charts.
the ppt design has to reflect the company colors in the logo with the logo scattered to show it is done by the company.

It Company

```html
<!DOCTYPE html>
<html lang="en">
<head>
<meta charset="utf-8">
<title>Social Media Agency – Slide Template</title>
<link rel="stylesheet" href="https://fonts.googleapis.com/css2?family=Questrial&family=Comfortaa:wght@600&display=swap">
<style>
  :root {
    --stage-black: #050505;
    --floor-dark: #5d6161;
    --floor-light: #c9cdcd;
    --frame-grey: #8d8d8d;
    --screen-black: #0c0c0c;
    --rod-light: #d4d6d6;
    --rod-shade: #8f9393;
    --cube-grey: #c6cdcc;
    --cube-grey-shade: #a9b0af;
    --cube-blue: #7b81bf;
    --cube-blue-shade: #5f65a3;
    --podium-blue: #5660a0;
    --podium-rim: #6a74b4;
    --podium-text: #1b1e33;
    --title-white: #f4f4f4;
  }
  html, body { margin: 0; padding: 0; overflow: hidden; background: var(--stage-black); }
  .slide {
    position: relative;
    width: 1200px;
    height: 675px;
    overflow: hidden;
    background: linear-gradient(to bottom,
      var(--stage-black) 0px, var(--stage-black) 190px,
      var(--floor-dark) 250px, var(--floor-light) 675px);
  }
  .rod {
    position: absolute;
    left: 0;
    height: 28px;
    background: linear-gradient(to bottom, var(--rod-light), var(--rod-shade));
  }
  .rod--upper { top: 125px; width: 250px; }
  .rod--lower { top: 415px; width: 160px; }
  .screen {
    position: absolute;
    left: 246px; top: 37px;
    width: 712px; height: 483px;
    background: var(--frame-grey);
    box-sizing: border-box;
    padding: 15px 9px 6px 16px;
  }
  .screen__panel {
    width: 100%; height: 100%;
    background: var(--screen-black);
  }
  .sheet-title {
    position: absolute;
    left: 0; right: 0; top: 62px;
    margin: 0;
    text-align: center;
    font-family: "Questrial", sans-serif;
    font-weight: 400;
    font-size: 62px;
    letter-spacing: 1px;
    color: var(--title-white);
    text-shadow: 0 3px 3px rgba(0,0,0,0.6);
  }
  .podium { position: absolute; left: 0; top: 0; }
  .podium__label {
    position: absolute;
    left: 360px; top: 585px;
    width: 440px;
    margin: 0;
    text-align: center;
    font-family: "Comfortaa", sans-serif;
    font-weight: 600;
    font-size: 40px;
    letter-spacing: -1px;
    color: var(--podium-text);
  }
  .cube {
    position: absolute;
    box-sizing: border-box;
  }
  .cube--grey { background: linear-gradient(135deg, var(--cube-grey) 60%, var(--cube-grey-shade)); }
  .cube--blue { background: linear-gradient(135deg, var(--cube-blue) 60%, var(--cube-blue-shade)); }
  .cube--left   { left: 155px;  top: 383px; width: 140px; height: 119px; }
  .cube--front  { left: 877px;  top: 420px; width: 93px;  height: 105px; }
  .cube--stack1 { left: 1048px; top: 53px;  width: 124px; height: 116px; }
  .cube--stack2 { left: 1022px; top: 169px; width: 131px; height: 105px; }
  .cube--stack3 { left: 989px;  top: 265px; width: 147px; height: 107px; }
  .cube--stack4 { left: 1001px; top: 370px; width: 119px; height: 110px; }
  .cube--stack5 { left: 1006px; top: 480px; width: 142px; height: 101px; }
</style>
</head>
<body>
  <main class="slide">
    <div class="rod rod--upper"></div>
    <div class="rod rod--lower"></div>

    <section class="screen">
      <div class="screen__panel"></div>
    </section>
    <h1 class="sheet-title">Sheet Title</h1>

    <svg class="podium" width="1200" height="675" viewBox="0 0 1200 675" aria-hidden="true">
      <path d="M197,506 Q600,600 994,462 L994,474 Q600,612 197,518 Z" fill="var(--podium-rim)"/>
      <path d="M197,518 Q600,612 994,474 L994,553 Q600,705 197,580 Z" fill="var(--podium-blue)"/>
    </svg>
    <p class="podium__label">Social Media Agency</p>

    <div class="cube cube--grey cube--left"></div>
    <div class="cube cube--grey cube--front"></div>

    <div class="cube cube--grey cube--stack1"></div>
    <div class="cube cube--blue cube--stack2"></div>
    <div class="cube cube--grey cube--stack3"></div>
    <div class="cube cube--blue cube--stack4"></div>
    <div class="cube cube--grey cube--stack5"></div>
  </main>
</body>
</html>
```